New design for www.TrimTable.com

On TrimTable you can find & book your hairdresser. TrimTable is the biggest platform in the Netherlands.

- The design should be a responcive design
- Should be able to go global, should fit in perfectly between all the big booking platforms like roomquay, zipvan etc,
- Should have te result of more bookings. :)
- We are ‘only’ asking a beautiful design, not a technical solution.
- We need a homepage (https://trimtable.com/), search resultpage ((https://trimtable.com/kapper/amsterdam/#), salonpage (https://trimtable.com/kapper/vorden/sol-mira-hair/), about us page (https://trimtable.com/aboutus/), for the hairdresser info page (https://trimtable.com/kapper/), login/register page (https://trimtable.com/account/signin/).

- On the page of the hairdresser there is a dynamic part. The part where you create your appointment. Please take a look at this part too after you choose your treatment (behandeling), employee (medewerker), Date (datum) and time (tijd). The part that you see after this, is the part where you fill in your data as a consumer.

I've added more logo's but mostly we use the green color.

A few of our competitors: www.glowpick.com, www.kestoly.com

Target Market(s)

All consumers

Industry/Entity Type

Hair And Beauty

Number of Pages Required

5+ page

Font styles to use
Sans Serif

Colors
abd036
c3c3c3
757575

Requirements
Must have
• Responsive
• We did an A/B test with the homepage. It turns out that option B works better then option A (take a look at the uploaded pictures). So what we need on the homepage: The USP's with the green checkboxes, The search button needs to by dynamic (changes for example from light green to dark green so you can see you can click it) The call to action sentence Zoek & Vind je kapsalon, the searchfield and searchbutton should be seperated.
Nice to have
• The style that we like is the flat design style. The website should be simple, clean and it should feel a bit like a luxury thing. Because an appointment with the hairdresser can be a real treat and luxury moment for yourself.
• The luxury feeling and flat design that is in the www.zipvan.com website is really nice for example. But then it has to be a bit more light and not so black and dark.

```html
<!DOCTYPE html>
<html lang="nl">
<head>
<meta charset="utf-8">
<title>TrimTable – Vind &amp; boek je kapper</title>
<link rel="stylesheet" href="https://fonts.googleapis.com/css2?family=Montserrat:wght@400;600;700&family=Open+Sans:wght@400;600&display=swap">
<style>
:root{
  --green:#abd036;
  --green-dark:#8fb126;
  --light:#c3c3c3;
  --mid:#757575;
  --ink:#1c1c1c;
  --night:#232323;
  --white:#ffffff;
  --paper:#f7f7f7;
}
*{margin:0;padding:0;box-sizing:border-box}
html,body{width:1200px;height:2608px;overflow:hidden}
body{font-family:"Open Sans",Arial,sans-serif;color:var(--mid);background:var(--white);position:relative}
.caps{font-family:"Montserrat",Arial,sans-serif;text-transform:uppercase;letter-spacing:.12em}
svg{display:block}

/* hero */
.hero{position:absolute;left:0;top:0;width:1200px;height:620px;overflow:hidden}
.hero-photo{position:absolute;inset:0;background:radial-gradient(ellipse 340px 420px at 600px 250px,#5a5a5a 0%,#3a3a3a 45%,#1f1f1f 100%)}
.hero-shade{position:absolute;inset:0;background:rgba(0,0,0,.25)}
.account-nav{position:absolute;top:16px;right:96px;display:flex;gap:8px}
.account-nav a{font-size:9px;color:var(--white);text-decoration:none;padding:6px 10px;font-weight:600}
.account-nav .register{border:1px solid rgba(255,255,255,.7)}
.brand{position:absolute;top:168px;left:0;width:1200px;display:flex;justify-content:center;align-items:center;gap:10px}
.brand-mark{width:36px;height:36px;border-radius:50%;background:var(--white)}
.brand-name{font-family:"Montserrat",Arial,sans-serif;font-weight:700;font-size:30px;color:var(--white);letter-spacing:-.01em}
.hero-scissors{position:absolute;top:232px;left:588px}
.tagline{position:absolute;top:272px;left:0;width:1200px;text-align:center;color:var(--white);font-size:12px;line-height:18px;font-weight:600}
.search-field{position:absolute;top:352px;left:432px;width:336px;height:46px;border:1px solid rgba(255,255,255,.85);display:flex;align-items:center;justify-content:center;color:var(--white);font-size:9px}
.search-button{position:absolute;top:440px;left:578px;width:44px;height:28px;border:1px solid rgba(255,255,255,.85);background:transparent;color:var(--white);font-size:9px;display:flex;align-items:center;justify-content:center}
.slider-arrows{position:absolute;right:48px;top:528px;display:flex;flex-direction:column;gap:8px}
.slider-arrows span{width:20px;height:20px;border:1px solid rgba(255,255,255,.6);display:flex;align-items:center;justify-content:center}

/* stats */
.stats{position:absolute;top:620px;left:0;width:1200px;height:330px;background:var(--white);display:grid;grid-template-columns:repeat(5,184px);padding:128px 0 0 80px}
.stat{text-align:center}
.stat-number{font-family:"Montserrat",Arial,sans-serif;font-weight:600;font-size:24px;color:var(--green)}
.stat svg{margin:10px auto 10px}
.stat-label{font-size:8px;color:var(--mid)}

/* app band */
.app-band{position:absolute;top:950px;left:0;width:1200px;height:255px;background:var(--night);overflow:hidden}
.app-photo{position:absolute;left:640px;top:0;width:560px;height:255px;background:linear-gradient(110deg,var(--night) 0%,#3b3b3b 40%,#2a2a2a 100%)}
.app-copy{position:absolute;left:140px;top:114px;width:440px}
.app-title{font-family:"Montserrat",Arial,sans-serif;font-weight:700;font-size:14px;color:var(--green);text-transform:uppercase;letter-spacing:.04em}
.app-text{margin-top:10px;font-size:9px;line-height:15px;color:var(--light)}
.app-button{position:absolute;left:140px;top:218px;border:1px solid var(--light);color:var(--white);font-size:9px;padding:9px 12px;font-family:"Montserrat",Arial,sans-serif;font-weight:600;letter-spacing:.04em}

/* steps */
.steps{position:absolute;top:1205px;left:0;width:1200px;height:850px;background:var(--white)}
.steps-photo{position:absolute;left:460px;top:245px;width:280px;height:545px;background:linear-gradient(180deg,#4b4b4b 0%,#2f2f2f 55%,#1d1d1d 100%)}
.step-box{position:absolute;border:2px solid var(--green);background:rgba(255,255,255,.94);display:flex;align-items:center;padding:0 22px;font-size:10px;line-height:16px;color:var(--green);font-weight:600}
.step-find{left:160px;top:267px;width:300px;height:120px}
.step-book{left:620px;top:415px;width:440px;height:120px;padding-left:140px}
.step-enjoy{left:152px;top:563px;width:348px;height:115px}
.step-icon{position:absolute}

/* footer */
.footer{position:absolute;top:2055px;left:0;width:1200px;height:553px;background:var(--ink);overflow:hidden;color:var(--light)}
.footer-photo{position:absolute;right:0;top:210px;width:330px;height:343px;background:radial-gradient(ellipse at 70% 60%,#3a3a3a 0%,var(--ink) 75%)}
.footer-brand{position:absolute;left:320px;top:80px}
.footer-brand h3,.footer-business h3{font-family:"Montserrat",Arial,sans-serif;font-size:10px;font-weight:700;color:var(--white);letter-spacing:.08em}
.footer-brand p{font-size:8px;line-height:13px;margin-top:4px}
.socials{position:absolute;left:540px;top:88px;display:flex;gap:10px}
.socials span{width:26px;height:26px;border-radius:50%;border:1px solid var(--light)}
.footer-business{position:absolute;left:680px;top:80px;width:220px}
.footer-business p{font-size:8px;line-height:13px;margin-top:4px}
.footer-scissors{position:absolute;left:588px;top:208px}
.popular{position:absolute;left:140px;top:304px;width:300px}
.popular h4{font-family:"Montserrat",Arial,sans-serif;font-size:8px;color:var(--white);letter-spacing:.06em;margin-bottom:10px}
.popular p{font-size:7px;line-height:11px;color:var(--mid)}
.city-links{position:absolute;left:560px;top:304px;display:grid;grid-template-columns:repeat(5,104px);row-gap:10px;list-style:none}
.city-links li{font-size:7px;color:var(--mid);text-transform:uppercase;letter-spacing:.05em}
.copyright{position:absolute;left:0;bottom:14px;width:1200px;text-align:center;font-size:7px;color:var(--mid)}
</style>
</head>
<body>

<header class="hero">
  <div class="hero-photo" role="img" aria-label="Dark portrait photo of a man with a styled haircut"></div>
  <div class="hero-shade"></div>
  <nav class="account-nav caps">
    <a href="#" class="login">Login</a>
    <a href="#" class="register">Register</a>
  </nav>
  <div class="brand">
    <span class="brand-mark"></span>
    <span class="brand-name">TrimTable</span>
  </div>
  <svg class="hero-scissors" width="24" height="24" viewBox="0 0 24 24" fill="none" stroke="#abd036" stroke-width="1.6"><circle cx="6" cy="18" r="3"/><circle cx="18" cy="18" r="3"/><path d="M8 16 18 3M16 16 6 3"/></svg>
  <p class="tagline caps">De grootste kappersboekingssite<br>van Nederland met 543 kappers</p>
  <div class="search-field caps">Voer je woonplaats in</div>
  <div class="search-button caps">Zoek</div>
  <div class="slider-arrows">
    <span><svg width="8" height="8" viewBox="0 0 8 8"><path d="M1 5.5 4 2.5 7 5.5" stroke="#fff" fill="none"/></svg></span>
    <span><svg width="8" height="8" viewBox="0 0 8 8"><path d="M1 2.5 4 5.5 7 2.5" stroke="#fff" fill="none"/></svg></span>
  </div>
</header>

<section class="stats">
  <div class="stat"><div class="stat-number">543</div><svg width="20" height="20" viewBox="0 0 24 24" fill="none" stroke="#757575" stroke-width="1.6"><circle cx="6" cy="18" r="3"/><circle cx="18" cy="18" r="3"/><path d="M8 16 18 3M16 16 6 3"/></svg><div class="stat-label caps">Kapperszaken</div></div>
  <div class="stat"><div class="stat-number">16.233</div><svg width="20" height="20" viewBox="0 0 24 24" fill="none" stroke="#757575" stroke-width="1.6"><circle cx="6" cy="18" r="3"/><circle cx="18" cy="18" r="3"/><path d="M8 16 18 3M16 16 6 3"/></svg><div class="stat-label caps">Behandelingen aangeboden</div></div>
  <div class="stat"><div class="stat-number">573.559</div><svg width="20" height="20" viewBox="0 0 24 24" fill="none" stroke="#757575" stroke-width="1.6"><circle cx="6" cy="18" r="3"/><circle cx="18" cy="18" r="3"/><path d="M8 16 18 3M16 16 6 3"/></svg><div class="stat-label caps">Afspraken gemaakt</div></div>
  <div class="stat"><div class="stat-number">7.192</div><svg width="20" height="20" viewBox="0 0 24 24" fill="none" stroke="#757575" stroke-width="1.6"><circle cx="6" cy="18" r="3"/><circle cx="18" cy="18" r="3"/><path d="M8 16 18 3M16 16 6 3"/></svg><div class="stat-label caps">Leden tevreden</div></div>
  <div class="stat"><div class="stat-number">27.003</div><svg width="20" height="20" viewBox="0 0 24 24" fill="none" stroke="#757575" stroke-width="1.6"><circle cx="6" cy="18" r="3"/><circle cx="18" cy="18" r="3"/><path d="M8 16 18 3M16 16 6 3"/></svg><div class="stat-label caps">Betrouwbare reviews</div></div>
</section>

<section class="app-band">
  <div class="app-photo" role="img" aria-label="Photo of a smartphone showing the app, lying on a dark table"></div>
  <div class="app-copy">
    <h2 class="app-title">Alle kappers van Nederland in je broekzak?</h2>
    <p class="app-text">Download nu de gratis app en boek altijd en overal je volgende afspraak bij<br>jouw favoriete kapper in een paar tikken.</p>
  </div>
  <div class="app-button">DOWNLOAD MOBILE APP</div>
</section>

<section class="steps">
  <div class="steps-photo" role="img" aria-label="Black and white photo of a man with a fresh haircut"></div>
  <div class="step-box step-find caps">Zoek &amp; vind je kapsalon</div>
  <div class="step-box step-book caps">Boek online je afspraak<br>met één knopdruk</div>
  <div class="step-box step-enjoy caps">Geniet van je nieuwe kapsel</div>
  <svg class="step-icon" style="left:578px;top:305px" width="44" height="34" viewBox="0 0 44 34" fill="#abd036"><rect x="4" y="4" width="14" height="8" rx="2"/><rect x="26" y="4" width="14" height="8" rx="2"/><circle cx="11" cy="22" r="10"/><circle cx="33" cy="22" r="10"/><rect x="18" y="14" width="8" height="8"/><circle cx="11" cy="22" r="5" fill="#2f2f2f"/><circle cx="33" cy="22" r="5" fill="#2f2f2f"/></svg>
  <svg class="step-icon" style="left:668px;top:460px" width="40" height="32" viewBox="0 0 40 32" fill="none" stroke="#abd036" stroke-width="2.4"><rect x="4" y="2" width="32" height="22"/><path d="M0 29h40"/><path d="M23 8h-5a2 2 0 0 0 0 4h4a2 2 0 0 1 0 4h-5M20 6v12"/></svg>
  <svg class="step-icon" style="left:512px;top:612px" width="40" height="40" viewBox="0 0 40 40" fill="#abd036"><path d="M20 4c-9 0-14 6-14 14 0 6 3 10 3 14h22c0-4 3-8 3-14 0-8-5-14-14-14z"/><rect x="14" y="32" width="12" height="6"/></svg>
</section>

<footer class="footer">
  <div class="footer-photo" role="img" aria-label="Photo of a barber trimming a client's hair"></div>
  <div class="footer-brand">
    <h3>TRIMTABLE</h3>
    <p>020 555 0134<br>hallo@trimtable.com</p>
  </div>
  <div class="socials"><span></span><span></span><span></span></div>
  <div class="footer-business">
    <h3>VOOR DE ONDERNEMER</h3>
    <p>Is jouw kapsalon nog niet aangesloten?<br>Meld je gratis aan en ontvang meer boekingen.</p>
  </div>
  <svg class="footer-scissors" width="24" height="24" viewBox="0 0 24 24" fill="none" stroke="#c3c3c3" stroke-width="1.4"><circle cx="6" cy="18" r="3"/><circle cx="18" cy="18" r="3"/><path d="M8 16 18 3M16 16 6 3"/></svg>
  <div class="popular">
    <h4>VAAK GEZOCHT: KAPPERS IN DE GROOTSTE PLAATSEN</h4>
    <p>Wil je snel een kapper vinden in jouw stad? Bekijk hier de populairste plaatsen van Nederland. Vergelijk salons, lees eerlijke reviews van andere klanten, bekijk prijzen en behandelingen en boek direct online een vrij moment dat jou goed uitkomt. Zo heb je altijd een afspraak, zonder te bellen en zonder wachten.</p>
  </div>
  <ul class="city-links">
    <li>Kapper Amsterdam</li><li>Kapper Utrecht</li><li>Kapper Almere</li><li>Kapper Breda</li><li>Kapper Zwolle</li>
    <li>Kapper Rotterdam</li><li>Kapper Eindhoven</li><li>Kapper Groningen</li><li>Kapper Tilburg</li><li>Kapper Leiden</li>
    <li>Kapper Den Haag</li><li>Kapper Nijmegen</li><li>Kapper Arnhem</li><li>Kapper Haarlem</li><li>Kapper Vorden</li>
  </ul>
  <p class="copyright">© TrimTable 2024</p>
</footer>

</body>
</html>
```